Large Christian Church organization website design

This website design is an advanced design ultimately requiring design for at least 4 pages, but starting with only one.

I am looking for an "award winning" design. I have made this easy as I have the functionality and general flow prototyped in an HTML prototype. I recorded videos to explain these in depth and will attach the HTML prototype as well.

The design must focused on connecting with people who need physical, emotional or spiritual help. It will be a website designed to meet people where they are and to help bring them along in there relationship to God.

Please work on this design only if you have a heart for people connecting with Christians and God.

A couple designers have asked me about the brief... did you have trouble downloading the brief for this project from this page:

If so, perhaps you can email me directly and I can send to you... you can email me: dmitri@pewlantern.org.
Also, would love to know if you still plan on creating a design for this project, thanks!

Reason: Still looking for a design that matches the functionality we need and provides a fantastic home run look and feel that is warm, inviting and friendly...

Reason: Need more time to provide feedback, request edits...

Target Market(s)

See creative brief

Industry/Entity Type

Church

Requirements
Must have
• The latest creative brief can be found here:

https://files.velmora.net/a/quostrel.com/sheet/d/7H3kPzW2mQ9rTx4LbN8vYcJ5dFa0GsE1uRoKi6wq/view?hl=en_US#mark=id.tqzlowhrva7k

```html
<!DOCTYPE html>
<html lang="en">
<head>
<meta charset="utf-8">
<title>Prairie Hills Conference</title>
<link rel="stylesheet" href="https://fonts.googleapis.com/css2?family=Play:wght@400;700&family=Cormorant+Garamond:wght@700&display=swap">
<style>
:root{
  --topbar:#262626;
  --topbar-line:#f2f2f2;
  --amber:#f3a514;
  --amber-light:#f7bd22;
  --amber-deep:#e08e0c;
  --footer:#dba217;
  --nav:#fdd57a;
  --nav-light:#fee9b4;
  --red:#c4141b;
  --red-dark:#8e0b10;
  --dark:#333333;
  --ink:#3a2a08;
  --link:#4a3506;
  --caption:#f4c04a;
  --thumb-label:#f6f09a;
  --divider:#b9860f;
}
*{box-sizing:border-box;margin:0;padding:0}
html,body{width:1200px;height:751px;overflow:hidden}
body{font-family:"Play",sans-serif;background:radial-gradient(ellipse at 50% 40%,var(--amber-light) 0%,var(--amber) 55%,var(--amber-deep) 100%);position:relative;color:var(--ink)}
.topbar{position:absolute;left:0;top:0;width:1200px;height:34px;background:var(--topbar);border-bottom:2px solid var(--topbar-line)}
.follow{position:absolute;left:588px;top:9px;font-size:13px;font-weight:700;color:#e8e8e8}
.social{position:absolute;top:8px;display:flex;gap:5px;left:654px}
.social span{width:18px;height:18px;border-radius:3px;background:#9aa4b0}
.search{position:absolute;left:801px;top:7px;width:168px;height:21px;border-radius:3px;background:linear-gradient(#fff,#e4e4e4);font-size:11px;color:#888;padding:4px 0 0 26px}
.search svg{position:absolute;left:7px;top:4px}
.go{position:absolute;left:976px;top:7px;width:37px;height:22px;border-radius:3px;background:linear-gradient(var(--red),var(--red-dark));color:#fff;font-size:12px;font-weight:700;text-align:center;line-height:22px}
.brand{position:absolute;left:190px;top:52px;display:flex;align-items:center;gap:8px}
.brand-mark{width:14px;height:14px;background:var(--red)}
.brand-name{font-size:15px;color:var(--ink);line-height:1.1}
.nav{position:absolute;left:184px;top:133px;width:824px;height:50px;background:linear-gradient(var(--nav-light),var(--nav));border-radius:4px 4px 0 0}
.menu-btn{position:absolute;top:9px;height:34px;border-radius:3px;color:#fff;font-size:12.5px;font-weight:700;letter-spacing:.5px;line-height:34px;padding-left:10px}
.menu-btn i{position:absolute;right:0;top:0;width:27px;height:34px;border-left:1px solid rgba(0,0,0,.35);font-style:normal;text-align:center;font-size:10px}
.menu-welcome{left:10px;width:139px;background:linear-gradient(#d81d22,var(--red-dark))}
.menu-church{left:164px;width:139px;background:linear-gradient(#4a4a4a,#1e1e1e)}
.nav-links{position:absolute;right:0;top:10px;display:flex}
.nav-links a{display:block;font-size:13px;color:var(--ink);text-decoration:none;padding:0 19px;height:31px;line-height:31px;border-left:1px solid #e2a637}
.nav-links a:first-child{border-left:none}
.hero{position:absolute;left:184px;top:183px;width:824px;height:277px;background:radial-gradient(ellipse at 55% 35%,#8c6f5a 0%,#4b4030 40%,#2d3a1e 75%,#1f2a16 100%)}
.caption{position:absolute;left:0;top:217px;width:499px;height:47px;background:rgba(30,28,24,.78);font-family:"Cormorant Garamond",serif;font-weight:700;font-size:28px;color:var(--caption);padding:5px 0 0 12px}
.dots{position:absolute;right:10px;top:257px;display:flex;gap:4px}
.dots span{width:11px;height:11px;border-radius:50%;background:#fff}
.dots span.active{background:#fff;box-shadow:inset 0 0 0 3px #fff,inset 0 0 0 6px #e58a0c}
.thumbs{position:absolute;left:181px;top:476px;display:flex;gap:11px}
.thumb{width:129px;height:120px;background:var(--thumb-label);border:1px solid #e0b94a;border-radius:2px;padding:2px}
.thumb-img{height:84px}
.thumb p{font-size:10.5px;text-align:center;color:var(--link);line-height:12px;height:30px;display:flex;align-items:center;justify-content:center}
.footer{position:absolute;left:0;top:614px;width:1200px;height:137px;background:var(--footer)}
.col{position:absolute;top:10px;height:118px;border-left:1px solid var(--divider);padding-left:17px}
.col h3{font-size:13px;font-weight:700;color:var(--ink);margin-bottom:1px}
.col a{display:block;font-size:10.8px;color:var(--link);text-decoration:none;line-height:15.2px}
</style>
</head>
<body>
<header class="topbar">
  <span class="follow">Follow us:</span>
  <div class="social"><span></span><span></span><span></span><span></span><span></span><span></span></div>
  <div class="search"><svg width="12" height="12" viewBox="0 0 12 12"><circle cx="7" cy="5" r="3.5" fill="none" stroke="#666" stroke-width="1.4"/><line x1="4.5" y1="7.5" x2="1" y2="11" stroke="#666" stroke-width="1.6"/></svg>Search...</div>
  <div class="go">Go</div>
</header>

<div class="brand">
  <span class="brand-mark"></span>
  <span class="brand-name">Prairie Hills Conference<br>of The Covenant Fellowship</span>
</div>

<nav class="nav">
  <div class="menu-btn menu-welcome">WELCOME MENU<i>&#8744;</i></div>
  <div class="menu-btn menu-church">CHURCH MENU<i>&#8744;</i></div>
  <div class="nav-links"><a href="#">PCF News</a><a href="#">PHC News</a><a href="#">Events</a><a href="#">Employment</a></div>
</nav>

<section class="hero" role="img" aria-label="Photo of a man embracing two children outdoors">
  <div class="caption">Changing lives all over North Texas...</div>
  <div class="dots"><span class="active"></span><span></span><span></span><span></span><span></span><span></span></div>
</section>

<section class="thumbs">
  <div class="thumb"><div class="thumb-img" role="img" aria-label="Photo of hands reaching through a barred window" style="background:linear-gradient(#6b4a35,#3a2a20)"></div><p>I need HELP...</p></div>
  <div class="thumb"><div class="thumb-img" role="img" aria-label="Photo of a man lifting his hands in prayer" style="background:linear-gradient(135deg,#f4f4f4,#c9a27a)"></div><p>I need GOD...</p></div>
  <div class="thumb"><div class="thumb-img" role="img" aria-label="Photo of a woman praying beside a tree" style="background:linear-gradient(135deg,#5d6a4a,#8a5a48)"></div><p>I need a CHURCH...</p></div>
  <div class="thumb"><div class="thumb-img" role="img" aria-label="Photo of a couple unpacking moving boxes" style="background:linear-gradient(135deg,#c9b79a,#8a7050)"></div><p>Moving to<br>NORTH TEXAS</p></div>
  <div class="thumb"><div class="thumb-img" role="img" aria-label="Photo of a white church building under blue sky" style="background:linear-gradient(#3d6fc4 0%,#8fb0df 45%,#e8e8e8 60%,#4f7a3a 100%)"></div><p>What is the<br>Covenant Fellowship?</p></div>
  <div class="thumb"><div class="thumb-img" role="img" aria-label="Photo of volunteers painting a brick house" style="background:linear-gradient(#9cc3e6 0%,#b25a3c 50%,#5d8a3a 100%)"></div><p>I &nbsp;want to SERVE</p></div>
</section>

<footer class="footer">
  <div class="col" style="left:259px"><h3>Category</h3><a href="#">Commonly Used Link</a><a href="#">Commonly Used Link</a><a href="#">Commonly Used Link</a><a href="#">Commonly Used Link</a><a href="#">Commonly Used Link</a><a href="#">Commonly Used Link</a></div>
  <div class="col" style="left:398px"><h3>Category</h3><a href="#">Commonly Used Link</a><a href="#">Commonly Used Link</a><a href="#">Commonly Used Link</a><a href="#">Commonly Used Link</a><a href="#">Commonly Used Link</a><a href="#">Commonly Used Link</a></div>
  <div class="col" style="left:534px"><h3>Category</h3><a href="#">Commonly Used Link</a><a href="#">Commonly Used Link</a><a href="#">Commonly Used Link</a><a href="#">Commonly Used Link</a><a href="#">Commonly Used Link</a><a href="#">Commonly Used Link</a></div>
  <div class="col" style="left:670px"><h3>Category</h3><a href="#">Commonly Used Link</a><a href="#">Commonly Used Link</a><a href="#">Commonly Used Link</a><a href="#">Commonly Used Link</a><a href="#">Commonly Used Link</a><a href="#">Commonly Used Link</a></div>
  <div class="col" style="left:806px"><h3>Category</h3><a href="#">Commonly Used Link</a><a href="#">Commonly Used Link</a><a href="#">Commonly Used Link</a><a href="#">Commonly Used Link</a><a href="#">Commonly Used Link</a><a href="#">Commonly Used Link</a></div>
</footer>
</body>
</html>
```